Tandra Link and recovery web and app design

GPS enabled APP providing breakdown and assistance for cyclists by cyclists.
24 hour bicycle assist and recovery package for both road and off road cyclists.
First and only bicycle assist package whose aim is to get you back on your bike to complete your journey

I need the design package to give a website designer so they can build website and app. I have a logo done by my nephew which is the company logo but i need a full design package now.

Below is the website banner I have now and the logo
Updates

Reason: I am moving house today and have no internet till Tuesday so please extend deadline 5 days to allow everyone

Target Market(s)

Cyclists in the South East and London, and then all UK, includes MTB off road and road cyclists. Please see farrowspinline.co.uk as this was my pretotype website for market information.

Number of Pages Required

5+ page

Font styles to use
Other font styles liked:
• FARROW SPINLINE

Colors
ffcf3e
f04b51
f68d4c
faa54b
fbee3f
add136

Requirements
Must have
• Landing page, mechanical page, medical page, FAQ page, policy information page accessible by policy holder to update, lost password page, quote page, pay page, contact us page, all policy info must be accessible by Norvane Desk out operations room provider,
Nice to have
• Lots of great action cycling photos and very usable website

```html
<!DOCTYPE html>
<html lang="en">
<head>
<meta charset="utf-8">
<title>Tandra Link UK – Cycle Mechanic Information</title>
<link rel="stylesheet" href="https://fonts.googleapis.com/css2?family=Roboto:wght@400;500;700&family=Open+Sans:wght@400;600&display=swap">
<style>
:root{
  --header-bg:#1e1c1b;
  --page-bg:#f1dfe1;
  --panel-bg:#ffffff;
  --band-top:#ffffff;
  --band-bottom:#ececec;
  --border:#e4e0e0;
  --text:#555555;
  --heading:#333333;
  --role:#2d3e57;
  --red:#e0343f;
  --accent:#e8505a;
  --orange:#f56a2a;
  --footer-bg:#3a3838;
  --footer-text:#e6e6e6;
}
*{box-sizing:border-box;margin:0;padding:0}
html,body{width:1200px;height:1162px;overflow:hidden}
body{background:var(--page-bg);font-family:"Open Sans",Arial,sans-serif;color:var(--text);position:relative}
.site-header{position:absolute;left:0;top:0;width:1200px;height:99px;background:var(--header-bg)}
.brand{position:absolute;left:110px;top:27px;display:flex;align-items:center;gap:14px}
.brand-dot{width:34px;height:34px;border-radius:50%;background:var(--accent)}
.brand-name{font-family:"Roboto",sans-serif;font-weight:700;font-size:31px;color:#d8d8d8;letter-spacing:.5px;border-top:1px solid #6a6a6a;border-bottom:1px solid #6a6a6a;padding:2px 0}
.main-nav{position:absolute;right:100px;top:29px;display:flex;align-items:center;gap:39px;font-family:"Roboto",sans-serif;font-size:14px}
.main-nav a{color:#fff;text-decoration:none}
.main-nav .signup{background:var(--orange);padding:9px 13px;border-radius:2px;margin-left:-7px}
.panel{position:absolute;left:99px;top:130px;width:1004px;height:941px;background:var(--panel-bg);border:1px solid var(--border)}
.panel-title{height:64px;background:linear-gradient(var(--band-top),var(--band-bottom));display:flex;align-items:center;justify-content:center;gap:10px;font-family:"Roboto",sans-serif;font-size:21px;color:var(--heading)}
.title-dot{width:14px;height:14px;border-radius:50%;border:2px solid var(--accent)}
.intro{position:absolute;left:36px;top:108px;width:932px;text-align:center;font-size:11.3px;line-height:20.6px}
.mechanic{position:absolute;width:461px;height:216px;border:1px solid var(--border);background:linear-gradient(90deg,#fff,#fafafa)}
.photo{position:absolute;left:9px;top:9px;width:180px;height:198px}
.info{position:absolute;left:211px;top:18px;width:231px}
.info h3{font-family:"Open Sans",sans-serif;font-weight:400;font-size:16px;color:var(--heading);margin-bottom:10px}
.role{display:flex;align-items:center;gap:10px;font-size:15px;color:var(--role);margin-bottom:8px}
.role .dot{width:11px;height:11px;border-radius:50%;border:2px solid var(--accent)}
.info p{font-size:11.4px;line-height:19.7px;text-align:justify}
.register{display:inline-block;margin-top:10px;background:var(--red);color:#fff;font-family:"Roboto",sans-serif;font-size:12.5px;padding:9px 15px;border-radius:2px}
.site-footer{position:absolute;left:0;top:1105px;width:1200px;height:57px;background:var(--footer-bg);color:var(--footer-text);font-size:12.5px;text-align:center;line-height:57px}
</style>
</head>
<body>
<header class="site-header">
  <div class="brand"><span class="brand-dot"></span><span class="brand-name">TANDRA LINK UK</span></div>
  <nav class="main-nav">
    <a href="#">HOME</a><a href="#">PACKAGE</a><a href="#">MOBILE APPS</a><a href="#">CONTACT</a><a href="#" class="signup">SIGN UP</a>
  </nav>
</header>

<main class="panel">
  <h1 class="panel-title"><span class="title-dot"></span>CYCLE MECHANIC INFORMATION</h1>
  <p class="intro">Sed ut perspiciatis unde omnis iste natus error sit voluptatem accusantium doloremque laudantium, totam rem aperiam, eaque ipsa quae ab illo inventore veritatis et quasi architecto beatae vitae dicta sunt explicabo. Nemo enim ipsam voluptatem quia voluptas sit aspernatur aut odit aut fugit, sed quia consequuntur magni dolores eos qui ratione voluptatem sequi nesciunt. Neque porro quisquam est, qui dolorem ipsum quia dolor sit amet, consectetur, adipisciquatur,</p>

  <article class="mechanic" style="left:27px;top:201px">
    <div class="photo" role="img" aria-label="Smiling mechanic in blue cap and overalls holding a tablet" style="background:linear-gradient(160deg,#8a94a2,#2f4a78 60%,#34507e)"></div>
    <div class="info"><h3>JOHN SMITH</h3><div class="role"><span class="dot"></span>Cycle Mechanics</div><p>Lorem ipsum dolor sit amet, consectetur adipiscing elit, sed do eiusmod tempor incididunt ut labore et dolore magna aliqua. Ut enim ad minim veniam,</p><span class="register">REGISTER NOW</span></div>
  </article>
  <article class="mechanic" style="left:514px;top:201px">
    <div class="photo" role="img" aria-label="Mechanic in blue overalls giving a thumbs up holding a wrench" style="background:linear-gradient(160deg,#c9c9c9,#2a5fb0 65%,#2456a6)"></div>
    <div class="info"><h3>JOHN SMITH</h3><div class="role"><span class="dot"></span>Cycle Mechanics</div><p>Lorem ipsum dolor sit amet, consectetur adipiscing elit, sed do eiusmod tempor incididunt ut labore et dolore magna aliqua. Ut enim ad minim veniam,</p><span class="register">REGISTER NOW</span></div>
  </article>
  <article class="mechanic" style="left:27px;top:441px">
    <div class="photo" role="img" aria-label="Mechanic with crossed arms holding a spanner in a workshop" style="background:linear-gradient(160deg,#b8bec6,#2e3450 60%,#3a3f58)"></div>
    <div class="info"><h3>JOHN SMITH</h3><div class="role"><span class="dot"></span>Cycle Mechanics</div><p>Lorem ipsum dolor sit amet, consectetur adipiscing elit, sed do eiusmod tempor incididunt ut labore et dolore magna aliqua. Ut enim ad minim veniam,</p><span class="register">REGISTER NOW</span></div>
  </article>
  <article class="mechanic" style="left:514px;top:441px">
    <div class="photo" role="img" aria-label="Senior mechanic in navy overalls with crossed arms holding a wrench" style="background:linear-gradient(160deg,#eeeeee,#d8d8d8 40%,#27325a 70%)"></div>
    <div class="info"><h3>JOHN SMITH</h3><div class="role"><span class="dot"></span>Cycle Mechanics</div><p>Lorem ipsum dolor sit amet, consectetur adipiscing elit, sed do eiusmod tempor incididunt ut labore et dolore magna aliqua. Ut enim ad minim veniam,</p><span class="register">REGISTER NOW</span></div>
  </article>
  <article class="mechanic" style="left:27px;top:681px">
    <div class="photo" role="img" aria-label="Young mechanic in blue dungarees and white t-shirt with crossed arms" style="background:linear-gradient(160deg,#5a5048,#e6e2dc 55%,#2c6fc0)"></div>
    <div class="info"><h3>JOHN SMITH</h3><div class="role"><span class="dot"></span>Cycle Mechanics</div><p>Lorem ipsum dolor sit amet, consectetur adipiscing elit, sed do eiusmod tempor incididunt ut labore et dolore magna aliqua. Ut enim ad minim veniam,</p><span class="register">REGISTER NOW</span></div>
  </article>
  <article class="mechanic" style="left:514px;top:681px">
    <div class="photo" role="img" aria-label="Smiling mechanic in blue jacket holding a spanner in a garage" style="background:linear-gradient(160deg,#e4e4e4,#c8c0b8 45%,#2c3f96 80%)"></div>
    <div class="info"><h3>JOHN SMITH</h3><div class="role"><span class="dot"></span>Cycle Mechanics</div><p>Lorem ipsum dolor sit amet, consectetur adipiscing elit, sed do eiusmod tempor incididunt ut labore et dolore magna aliqua. Ut enim ad minim veniam,</p><span class="register">REGISTER NOW</span></div>
  </article>
</main>

<footer class="site-footer">Copyright © Tandra Link UK. All rights reserved. Contact Us / T&amp;Cs / Privacy Policy</footer>
</body>
</html>
```